Wellness Web Design Project

web design for business called Lumen Harbor Wellness. I have a private practice for which i need patients. I teach in house and online courses for professional and the public. It will be both an educational site as well as a marketing site and it will have a store and a member login area. I do sonic acupuncture called vibrelaxis. It is based on demarchetos' music of the spheres. I use vibrational and harmonic therapies to harmonize cells psyches and souls! it is the most scientifically rooted of the alternative therapies available and i focus on womens health, pediatric, emotional problems and spiritual awakening. I need it to be a balance of spiritual and symbolic depth as well as being graceful sophisticated grounded. I want it to look incredibly elegant, sophisticated, and established, not airy fairy! i like a minimal approach, fresh air, clean, confident, expensive, luxurious but also playful. im not trying to mold myself into the usual framework. i am trying to convey a sense of unleashing power and purpose and pleasure. i need it to be Gorgeous and relatable while being original
i have included the site map as an upload and here is a link to all the things that a home page should include. I have the logo and other versions that i will use to promote the different online programs i have. I may have a 'sound logo' start as the page comes up. the sounds are ethereal tones rather than music and super gentle and mysterious without being cloying or overly emotional. I work with the physical body, emotional trauma and altered states so many hats and have many different prongs to what i do so organization and clarity is important without getting cluttered. want to convert and capture into my email list for sure and have free downloadable content to provide.
the logo i have designed speaks volumes about my aesthetic. i have included a flyer made - which is 1. direction, but i am interested in seeing some designs that play with white space as well. the 'look' of the flyer has never been published and so am in no way married to it. I will include some of the photo i will want to use along the way that give you some sense of things or things to riff off. some of the photos of me have alot of solid blocks of color... i have included one of them. I am very sensitive to sophistication of color.
the site map i have included is jsut my attempt to organize - i am not married to it!
thankyou so much, and if you haven;t yet discovered the power of sound to alter brain waves and cell functioning wherever you are in the world - I highly recommend it:)

Target Market(s)

women 25-55's educated, familiar with alternative healing and conscious living who have money to spend on wellness

Industry/Entity Type

Business

Requirements
Must have
• http://notes.brimfaldo.com/notes/tabid/4821/bid/58204/12-Critical-Elements-Every-Homepage-Must-Have-Infographic.aspx
these are some of the elements that seem to be necessary
plus social media links....

```html
<!DOCTYPE html>
<html lang="en">
<head>
<meta charset="utf-8">
<title>Lumen Harbor Wellness</title>
<link rel="stylesheet" href="https://fonts.googleapis.com/css2?family=Cinzel:wght@400&family=PT+Sans:wght@400&family=PT+Sans+Narrow:wght@400&display=swap">
<style>
:root{
  --mint-top:#c9eee4;
  --mint-bottom:#ade7d5;
  --green:#5a9e56;
  --teal:#72c3bf;
  --teal-dark:#5fb3ae;
  --ink:#5e6664;
  --ink-dark:#3f4a48;
  --muted:#8d9593;
  --white:#ffffff;
  --icon-grey:#cfd2d1;
}
*{box-sizing:border-box;margin:0;padding:0}
html,body{width:1200px;height:1038px;overflow:hidden}
body{
  position:relative;
  font-family:"PT Sans",sans-serif;
  color:var(--ink);
  background:linear-gradient(180deg,var(--mint-top) 0,#bfeade 170px,#b5e9d9 400px,var(--mint-bottom) 1038px);
}
.abs{position:absolute}
.header-rule{left:0;top:169px;width:1200px;height:4px;background:var(--green)}
.brand{left:128px;top:33px;width:305px;height:106px;background:var(--white);border-radius:8px;display:flex;align-items:center;gap:14px;padding-left:26px}
.brand-dot{width:30px;height:30px;border-radius:50%;background:var(--green)}
.brand-name{font-size:25px;color:var(--green);letter-spacing:-.2px}
.main-nav{left:559px;top:42px;display:flex;align-items:center;font-family:"PT Sans Narrow",sans-serif;font-size:18px;color:var(--ink);letter-spacing:.6px}
.main-nav a{color:inherit;text-decoration:none;margin-right:18px}
.main-nav .current{background:var(--white);color:var(--green);width:70px;height:34px;border-radius:3px;display:flex;align-items:center;justify-content:center;margin-right:17px}
.header-phone{left:716px;top:92px;display:flex;align-items:center;gap:10px;color:var(--white);font-size:20px;letter-spacing:1px}
.social{display:flex;gap:9px}
.social span{width:34px;height:34px;border-radius:50%;background:var(--teal);border:2px solid rgba(255,255,255,.7)}
.header-social{left:899px;top:88px}
.login{left:126px;top:189px;width:336px;height:227px;background:var(--white);border-radius:10px;padding:10px 18px 0 18px}
.panel-title{font-size:19px;letter-spacing:1.3px;color:var(--ink);font-weight:400;margin-left:2px}
.field{margin-top:9px;height:40px;border:1px solid #dcdcdc;border-radius:4px;background:linear-gradient(#f9f9f9,#ececec);display:flex;align-items:center;padding-left:16px;gap:14px;color:#b7b7b7;font-size:15px}
.field:first-of-type{margin-top:10px}
.login-btn{margin-top:6px;height:40px;border:1px solid #d4d4d4;border-radius:4px;background:linear-gradient(#fdfdfd,#ececec);text-align:center;line-height:38px;font-size:19px;letter-spacing:1.5px;color:var(--muted)}
.login-extra{display:flex;justify-content:space-between;align-items:center;margin-top:17px;font-size:13px;color:var(--muted);letter-spacing:.4px}
.remember{display:flex;align-items:center;gap:8px;margin-left:4px}
.box{width:15px;height:15px;background:#c9c9c9;border-radius:2px}
.forgot{color:#333;text-decoration:underline}
.promo{left:126px;top:433px;width:336px;height:114px;border-radius:3px;background:linear-gradient(100deg,#87b8aa,#b6dbd0 45%,#8fc0b2);display:flex;align-items:center;justify-content:center;text-align:center;font-family:"Cinzel",serif;font-size:19px;line-height:30px;color:var(--ink-dark);text-shadow:0 0 6px rgba(255,255,255,.9);letter-spacing:.3px}
.slider{left:478px;top:189px;width:588px;height:358px;border-radius:10px;overflow:hidden;border:1px solid #c5e6df;background:radial-gradient(ellipse at 55% 55%,#ffffff 0,#e6f7f4 45%,#c9ece6 100%)}
.slide-title{position:absolute;left:16px;top:12px;font-family:"Cinzel",serif;font-size:21px;color:var(--ink-dark);letter-spacing:.8px}
.slide-text{position:absolute;left:16px;top:43px;width:390px;font-size:13px;line-height:18px;color:#333;letter-spacing:.4px}
.slide-dots{position:absolute;left:217px;bottom:0;width:149px;height:29px;background:var(--teal);border-radius:6px 6px 0 0;display:flex;justify-content:center;align-items:center;gap:9px}
.slide-dots i{width:12px;height:12px;border-radius:50%;background:var(--white)}
.slide-dots i.on{background:#253532}
.slide-bar{position:absolute;left:0;bottom:0;width:100%;height:3px;background:var(--teal)}
.content{left:126px;top:564px;width:940px;height:279px;background:var(--white);border-radius:8px}
.section-title{font-size:19px;letter-spacing:1.4px;color:var(--ink);font-weight:400}
.copy{font-size:13px;letter-spacing:.6px;color:var(--ink)}
.healing{left:16px;top:20px}
.healing .copy{margin-top:19px;width:420px;line-height:23px}
.btn{position:absolute;height:34px;background:var(--teal);color:var(--white);border-radius:2px;font-size:15px;letter-spacing:.5px;display:flex;align-items:center;justify-content:center;width:104px}
.portrait{left:485px;top:16px;width:145px;height:197px;background:linear-gradient(160deg,#8aa056 0,#b69878 50%,#3b3a36 100%);border:1px solid #e6e6e6;box-shadow:0 10px 8px -6px rgba(0,0,0,.35)}
.about{left:649px;top:12px;width:270px}
.about .copy{line-height:22px}
.about .first{margin-top:24px;margin-left:2px}
.about .second{margin-top:12px}
.footer{left:126px;top:862px;width:940px;height:119px;background:var(--white);border-radius:8px}
.footer-nav{left:15px;top:9px;font-size:15px;letter-spacing:.5px;color:var(--ink)}
.footer-address{left:564px;top:8px;display:flex;align-items:center;gap:8px;font-size:15px;letter-spacing:.5px}
.footer-contact{left:17px;top:50px;display:flex;align-items:center;font-size:21px;letter-spacing:1px;color:var(--ink)}
.footer-contact .email{margin-left:18px;display:flex;align-items:center;gap:10px}
.footer-contact .phone{display:flex;align-items:center;gap:10px}
.footer-social{left:751px;top:53px}
.footer-social span{background:var(--icon-grey);border-color:#e3e3e3}
.copyright{left:0;top:98px;width:100%;text-align:center;font-family:Arial,sans-serif;font-size:11px;color:#555}
</style>
</head>
<body>

<div class="abs header-rule"></div>

<header>
  <div class="abs brand">
    <span class="brand-dot"></span>
    <span class="brand-name">Lumen Harbor Wellness</span>
  </div>
  <nav class="abs main-nav">
    <a class="current" href="#">Home</a>
    <a href="#">About</a>
    <a href="#" style="margin-right:22px">Vibrelaxis</a>
    <a href="#">Success Stories</a>
    <a href="#">Blog</a>
    <a href="#" style="margin-right:0">Testimonials</a>
  </nav>
  <div class="abs header-phone">
    <svg width="12" height="26" viewBox="0 0 12 26"><path d="M4 1h5v6H6c-.6 3-.6 9 0 12h3v6H4C1 22 0 17 0 13S1 4 4 1z" fill="#fff"/></svg>
    <span>310-555-0148</span>
  </div>
  <div class="abs social header-social" aria-label="Social links"><span></span><span></span><span></span><span></span></div>
</header>

<section class="abs login">
  <h2 class="panel-title">MEMBER LOGIN</h2>
  <div class="field">
    <svg width="18" height="18" viewBox="0 0 18 18"><circle cx="9" cy="5" r="4" fill="#bbb"/><path d="M1 17c0-5 4-7 8-7s8 2 8 7z" fill="#bbb"/></svg>
    <span>User Name</span>
  </div>
  <div class="field">
    <svg width="18" height="18" viewBox="0 0 18 18"><path d="M5 8V5a4 4 0 0 1 8 0v3" stroke="#bbb" stroke-width="2" fill="none"/><rect x="3" y="8" width="12" height="9" rx="1" fill="#bbb"/></svg>
    <span>Password</span>
  </div>
  <div class="login-btn">LOGIN</div>
  <div class="login-extra">
    <span class="remember"><span class="box"></span>Remember me</span>
    <span class="forgot">Forgot Password?</span>
  </div>
</section>

<div class="abs promo" role="img" aria-label="Soft teal light rays with sparkles behind the tagline">
  <p>HARMONIC THERAPIES TO<br>HARMONIZE CELLS PSYCHES<br>AND SOULS!</p>
</div>

<section class="abs slider" role="img" aria-label="Pale teal anatomical meridian sketch of a human figure">
  <h2 class="slide-title">Lorem Ipsum is simply dummy text</h2>
  <p class="slide-text">printing and typesetting industry. Lorem Ipsum has been the industry's standard dummy</p>
  <div class="slide-bar"></div>
  <div class="slide-dots"><i class="on"></i><i></i><i></i><i></i><i></i></div>
</section>

<main class="abs content">
  <article class="abs healing">
    <h2 class="section-title">HARMONIC SOUND HEALING</h2>
    <p class="copy">It is a long established fact that a reader will be distracted by the readable content of a page when looking at its layout. The point of using Lorem Ipsum is that it has a more-or-less normal distribution of letters, as opposed to using 'Content here, con-tent here', making it look like readable English. to using 'Content here Many desktop publishing packages and web page editors now use Lorem (injected humour and the like).</p>
  </article>
  <a class="btn" style="left:336px;top:226px">Read More</a>

  <div class="abs portrait" role="img" aria-label="Portrait photo of the practitioner outdoors"></div>
  <article class="abs about">
    <h2 class="section-title">ABOUT</h2>
    <p class="copy first">Dr. Wren Hollis is a doctor of Oriental Medicine, and a Senior and international teacher of Vibrelaxis. She works with trauma and mental health.</p>
    <p class="copy second">simply dummy text of the printing and typesetting industry. Lorem Ipsum has.</p>
  </article>
  <a class="btn" style="left:807px;top:226px">Read More</a>
</main>

<footer class="abs footer">
  <div class="abs footer-nav">Home | About | Vibrelaxis | Success Stories | Blog | Testimonials</div>
  <div class="abs footer-address">
    <svg width="36" height="34" viewBox="0 0 36 34"><path d="M2 18l14-6 18 8-14 7z" fill="#f1e3c4" stroke="#c9a96a"/><path d="M16 4a6 6 0 0 1 6 6c0 5-6 11-6 11s-6-6-6-11a6 6 0 0 1 6-6z" fill="#e0322c"/><circle cx="16" cy="10" r="2.2" fill="#fff"/></svg>
    <span>418C Marlow Ave, Seacliff, CA 90488</span>
  </div>
  <div class="abs footer-contact">
    <span class="phone">
      <svg width="12" height="26" viewBox="0 0 12 26"><path d="M4 1h5v6H6c-.6 3-.6 9 0 12h3v6H4C1 22 0 17 0 13S1 4 4 1z" fill="#777"/></svg>
      310-555-0148
    </span>
    <span class="email">
      <svg width="26" height="26" viewBox="0 0 26 26"><circle cx="13" cy="13" r="12" fill="#eee" stroke="#888" stroke-width="1.5"/><rect x="6" y="8.5" width="14" height="9" fill="none" stroke="#777" stroke-width="1.5"/><path d="M6 8.5l7 5 7-5" fill="none" stroke="#777" stroke-width="1.5"/></svg>
      wrenhollis@lumenmail.com
    </span>
  </div>
  <div class="abs social footer-social" aria-label="Social links"><span></span><span></span><span></span><span></span></div>
  <p class="abs copyright">© 2013 Lumen Harbor Wellness. All Rights Reserved.</p>
</footer>

</body>
</html>
```